Flyer-Design für Psychotherapeut
Zielgruppe
Angeboten wird als Dienstleistung Psychotherapie, Coaching und Paarberatung
für Einzelpersonen (Männer/Frauen), Paare und Familien in schwierigen privaten und beruflichen Lebenssituationen.
Aufgabenstellung
Sehr geehrte Damen, sehr geehrte Herren,
gewünscht wird ein Falzflyer Hochformat, DIN-Lang, Wickelfalz, 6 bedruckte Seiten mit dem Endformat 10,0 x 21,0 cm. Ein entsprechendes Datenblatt der Druckerei finden Sie im Anhang.
Der Flyer wird auf einer Gesundheitsmesse eingesetzt und soll einen Überblick über mein Dienstleistungsangebot geben.
In der beigefügten Word Datei finden Sie einen von mir erstellten Flyer-Text-Entwurf. Er soll lediglich als Orientierung dienen. Weitere Infos erhalten Sie auf meiner Homepage
www.praxis-tollring-quast.de.
Desweiteren erhalten Sie ein hochgeladenes Foto von mir, welches Sie bitte in Ihren Entwurf mit einbinden.
Ich bitte um Vorschläge für ein professionelles Design mit moderener gut lesbarer Schrift sowie farblich abgestimmten Blöcken des Inhalts.
Besonders wichtig ist mir die Orientierung an meinen Logofarben.
Das Logo wurde auch von gestaltwerk.de erstellt. Sie finden es unter meinen Projekten.
Für Rückfragen stehe ich Ihnen gerne zur Verfügung.
Freundliche Grüße
Sabine Tollring-Quast

```html
<!DOCTYPE html>
<html lang="de">
<head>
<meta charset="utf-8">
<title>Falzflyer Praxis Tollring-Quast</title>
<link href="https://fonts.googleapis.com/css2?family=Open+Sans:ital,wght@0,400;0,600;0,700;1,400;1,600;1,700&family=PT+Sans+Narrow:wght@400;700&display=swap" rel="stylesheet">
<style>
:root{
  --orange:#e8562a;
  --orange-deep:#d9461c;
  --grey:#8b8c8e;
  --grey-dark:#6f7072;
  --paper:#f4f4f4;
  --ink:#4a4a4a;
  --stage:#dcdcdc;
}
*{margin:0;padding:0;box-sizing:border-box}
html,body{width:1200px;height:960px;overflow:hidden}
body{background:var(--stage);font-family:"Open Sans",sans-serif;color:var(--ink);position:relative}
.spread{position:absolute;left:279px;width:642px;height:450px;display:flex;box-shadow:0 4px 14px rgba(0,0,0,.18)}
.spread--inside{top:20px}
.spread--outside{top:490px}
.panel{position:relative;width:214px;height:450px;background:var(--paper);overflow:hidden}
.panel + .panel{border-left:1px solid #e2e2e2}
.band-bottom{position:absolute;left:0;right:0;bottom:0;height:14px;background:var(--orange)}
ul{list-style:none}
li{position:relative;padding-left:11px}
li::before{content:"";position:absolute;left:1px;top:.55em;width:3px;height:3px;border-radius:50%;background:currentColor}
.bullets--orange li::before{background:var(--orange);width:4px;height:4px}

/* inside left */
.intro-block{background:var(--grey);color:#fff;padding:18px 12px 14px 14px;height:212px}
.intro-block h2{font-size:10px;font-weight:600;line-height:1.4;margin-bottom:10px}
.intro-block li{font-size:7.3px;line-height:1.45;margin-bottom:9px;padding-left:14px}
.intro-text{padding:16px 14px;font-size:7.6px;line-height:1.5;color:#333}
.intro-text p{margin-bottom:11px}

/* inside middle */
.offer{padding:18px 12px 0 12px;font-family:"PT Sans Narrow",sans-serif;height:272px}
.kicker{color:var(--orange);font-weight:700;font-size:9.5px;margin-bottom:3px}
.offer h3{font-size:9.5px;font-weight:700;color:#555;line-height:1.35;margin-bottom:14px}
.offer p{font-size:7.4px;line-height:1.55;margin-bottom:10px;color:#555}
.benefits{position:absolute;left:0;right:0;top:272px;bottom:14px;background:var(--orange);color:#fff;padding:16px 12px;font-family:"PT Sans Narrow",sans-serif}
.benefits h3{font-size:9.5px;font-weight:700;margin-bottom:10px}
.benefits li{font-size:7.6px;line-height:1.35;margin-bottom:1px}
.spread--inside .panel:nth-child(2) .band-bottom{background:var(--orange-deep)}

/* inside right */
.focus{padding:18px 12px 0 12px;height:172px}
.focus .kicker{font-family:"Open Sans",sans-serif;font-size:8.5px}
.focus h3{font-size:8.5px;font-weight:700;color:#555;margin-bottom:12px}
.focus li{font-size:7.2px;line-height:1.5;padding-left:22px;color:#555}
.focus li::before{left:6px}
.coaching{background:var(--grey);color:#fff;padding:12px 12px;height:176px}
.coaching .label{font-size:7.6px;font-weight:700;opacity:.9;margin-bottom:2px}
.coaching h3{font-size:7.8px;font-weight:700;line-height:1.35;margin-bottom:10px}
.coaching li{font-size:6.9px;line-height:1.4;padding-left:16px}
.growth{padding:12px 12px}
.growth h3{font-size:8px;font-weight:700;color:#555;margin-bottom:10px}
.growth li{font-size:7px;line-height:1.45;color:#555;padding-left:14px}

/* outside left */
.couples{padding:20px 12px 0 14px;height:234px}
.couples .kicker{font-family:"Open Sans",sans-serif;font-size:8.5px}
.couples h3{font-size:8.5px;font-weight:700;color:#555;margin-bottom:12px}
.couples li{font-size:7.4px;line-height:1.35;color:#666;margin-bottom:7px;padding-left:14px}
.mediation{background:var(--orange);color:#fff;padding:14px 14px;height:88px}
.mediation h3{font-size:9px;font-weight:700;margin-bottom:10px}
.mediation li{font-size:7.6px;padding-left:14px}

/* outside middle */
.top-strip{height:10px;background:var(--grey)}
.portrait{display:block;width:214px;height:142px}
.about{padding:12px 12px 0 14px;font-style:italic;font-size:7.3px;line-height:1.45;color:#333;height:148px}
.about p{margin-bottom:9px}
.about .quote{color:var(--orange);font-weight:700}
.about .ask{font-weight:600}
.contact{position:absolute;left:0;right:0;bottom:0;height:150px;background:var(--grey);color:#fff;padding:14px 14px;font-style:italic;font-size:7.4px;line-height:1.4}
.contact h3{font-size:8px;font-weight:700;font-style:italic}
.contact .address{margin-top:10px}

/* cover */
.brand{display:flex;align-items:flex-start;gap:8px;padding:32px 12px 0 14px}
.brand-dot{width:22px;height:22px;border-radius:50%;background:var(--orange);flex:none;margin-top:2px}
.brand-name{font-size:11.5px;font-weight:400;color:#555;line-height:1.25}
.brand-tag{font-size:6.4px;font-weight:600;color:var(--orange);margin-top:3px}
.claim{position:absolute;right:16px;top:150px;text-align:right;font-weight:700;font-size:14px;line-height:1.1;letter-spacing:.5px;color:#555}
.claim .hl{color:var(--orange)}
.headline{position:absolute;left:0;right:0;top:226px;height:112px;background:var(--orange);color:#fff;padding:24px 14px;font-weight:700;font-size:14.5px;line-height:1.35;text-align:center}
.tagline{position:absolute;left:0;right:0;top:360px;text-align:center;color:var(--orange);font-style:italic;font-weight:700;font-size:8.6px;line-height:1.4}
</style>
</head>
<body>

<section class="spread spread--inside">
  <article class="panel">
    <div class="intro-block">
      <h2>Sie wünschen sich Entlastung und positive Veränderung weil ....</h2>
      <ul>
        <li>Sie sich in einer akuten privaten oder beruflichen Krisensituation befinden.</li>
        <li>Sie Probleme in Ihrer Partnerschaft haben.</li>
        <li>Sie mit Stress besser umgehen wollen.</li>
        <li>Sie sich antriebslos- und lustlos, erschöpft oder ständig überfordert fühlen.</li>
        <li>Sie unter Ängsten oder Panikattacken leiden, die Sie belasten und einschränken.</li>
      </ul>
    </div>
    <div class="intro-text">
      <p>Jeder Mensch kommt im Leben in Situationen, die Unzufriedenheit, Überforderung und seelische Belastungen auslösen.</p>
      <p>Wenn Veränderung nicht alleine gelingt, können Psychotherapie, Coaching oder Paarberatung eine große Hilfe sein, um Lösungswege aus diesen belastenden Situationen zu finden.</p>
    </div>
    <div class="band-bottom"></div>
  </article>

  <article class="panel">
    <div class="offer">
      <div class="kicker">Mein Angebot für Sie</div>
      <h3>Beratung- und Gesprächstherapie nach Elias Brandt Systemisches Coaching und Paarberatung</h3>
      <p>Als erfahrene Therapeutin, Beraterin und Coach begleite ich Sie als Einzelperson, Paar oder Familie in schwierigen Lebenssituationen und Neuorientierungsphasen.</p>
      <p>Ich unterstütze Sie einfühlsam und lösungsorientiert. Dabei nutze ich anerkannte, wirksame Therapie- und Beratungsmethoden, die ich gemeinsam mit Ihnen, auf Ihre persönlichen Bedürfnisse und Ziele abstimme.</p>
      <p>Im Mittelpunkt stehen Sie mit Ihrem Anliegen. Wir begegnen uns in einer Atmosphäre der Wertschätzung, Anteilnahme und absoluten Diskretion.</p>
    </div>
    <div class="benefits">
      <h3>Sie können ...</h3>
      <ul>
        <li>Bewältigungsstrategien entwickeln</li>
        <li>Ihre Fähigkeiten und Stärken entdecken</li>
        <li>Innere Blockaden überwinden</li>
        <li>Ihr Selbstvertrauen steigern</li>
        <li>Sich mutig und motiviert an Neues heranwagen</li>
        <li>Ihre Ziele umsetzen</li>
        <li>Ihr Leben und Ihre Partnerschaft so gestalten, wie Sie es sich wünschen.</li>
      </ul>
    </div>
    <div class="band-bottom"></div>
  </article>

  <article class="panel">
    <div class="focus">
      <div class="kicker">Psychotherapie</div>
      <h3>Meine Behandlungsschwerpunkte:</h3>
      <ul class="bullets--orange">
        <li>Ängste- und Panikattacken</li>
        <li>Depression</li>
        <li>Erschöpfung/Burnout</li>
        <li>Reaktion auf schwere Belastungen</li>
        <li>Psychosomatische Beschwerden</li>
        <li>Psychoonkologie</li>
        <li>Lindauer Gesundheitstraining</li>
      </ul>
    </div>
    <div class="coaching">
      <div class="label">COACHING</div>
      <h3>Begleitung in Veränderungsprozessen und schwierigen Lebensphasen/-krisen</h3>
      <ul>
        <li>Veränderte Rahmenbedingungen im Privat- und Berufsleben, wie z.B. Krankheit, Trennung, Trauer, Mobbing, Arbeitsplatzverlust u.a.</li>
        <li>Berufliche Neuorientierung</li>
        <li>Entscheidungsfindung</li>
        <li>Zielsetzung und Realisierung</li>
        <li>Lebensumbrüche wie z.B. Wechseljahre, Pensionierung u.a.</li>
      </ul>
    </div>
    <div class="growth">
      <h3>Persönlichkeitsentwicklung</h3>
      <ul class="bullets--orange">
        <li>Konflikte erkennen und konstruktiv lösen</li>
        <li>Beziehungs- und Lebensgestaltung</li>
        <li>Eigene Stärken entdecken, weiter entwickeln und nutzen</li>
        <li>Stressbewältigung/Burnoutprävention</li>
      </ul>
    </div>
    <div class="band-bottom"></div>
  </article>
</section>

<section class="spread spread--outside">
  <article class="panel">
    <div class="couples">
      <div class="kicker">Paarberatung</div>
      <h3>Unterstützung für Paare in Krisenzeiten</h3>
      <ul class="bullets--orange">
        <li>wenn Sie das Gefühl haben aneinander vorbei zu reden</li>
        <li>wenn Ihr Beziehungsalltag von Streitereien und Konflikten bestimmt wird</li>
        <li>wenn Sie Ihre gemeinsame Intimität und Sexualität verloren haben</li>
        <li>wenn eine Affäre Ihre Beziehung erschüttert hat</li>
        <li>wenn das Leben in der Patchwork-Familie Ihre Beziehung belastet</li>
      </ul>
    </div>
    <div class="mediation">
      <h3>Trennungsbegleitung und Mediation</h3>
      <ul><li>wenn Sie über Trennung nachdenken</li></ul>
    </div>
    <div class="band-bottom"></div>
  </article>

  <article class="panel">
    <div class="top-strip"></div>
    <svg class="portrait" viewBox="0 0 214 142" role="img" aria-label="Porträtfoto der Therapeutin in Schwarzweiß">
      <defs>
        <linearGradient id="portraitTone" x1="0" y1="0" x2="1" y2="1">
          <stop offset="0" stop-color="#4a4a4a"/>
          <stop offset=".55" stop-color="#9a9a9a"/>
          <stop offset="1" stop-color="#3e3e3e"/>
        </linearGradient>
      </defs>
      <rect width="214" height="142" fill="url(#portraitTone)"/>
    </svg>
    <div class="about">
      <p>Weitere Informationen über mich und meine Angebote finden Sie auf meiner Homepage.</p>
      <p>Ich freue mich auf Ihren Besuch!</p>
      <p class="quote">„Jeder Weg beginnt mit dem ersten Schritt.“<br>(Meister Liu)</p>
      <p class="ask">Haben Sie Fragen?<br>Rufen Sie mich an. Ich bin für Sie da!</p>
    </div>
    <div class="contact">
      <h3>Kontakt</h3>
      <div>Sabine Tollring-Quast<br>Heilpraktikerin Psychotherapie (HeilprG)<br>Systemischer Coach (VSCD)</div>
      <div class="address">Am Lindenhof 14<br>64599 Waldbrunnach<br>Telefon 06155 – 472913<br>info@praxis-tollring-quast.de<br>www.praxis-tollring.de</div>
    </div>
  </article>

  <article class="panel">
    <div class="brand">
      <span class="brand-dot"></span>
      <div>
        <div class="brand-name">Sabine Tollring-Quast</div>
        <div class="brand-tag">Psychotherapie | Coaching | Paarberatung</div>
      </div>
    </div>
    <div class="claim">AUS<span class="hl">WEGE</span><br>LÖSU<span class="hl">NGSWEGE</span></div>
    <div class="headline">Für mehr Zufriedenheit im Privatleben und Beruf</div>
    <div class="tagline">... damit sich Ihre Lebensfreude<br>voll entfalten kann!</div>
    <div class="band-bottom"></div>
  </article>
</section>

</body>
</html>
```